BRYLTAllies.co.uk - Mental Health Clinic for Child and Adolescents

Updated 29/01/2018***
I am not sure you guys are getting the idea regards to the opening page / homescreen layout. Can you look at the new images I have uploaded (page 5, 6 and 7) These are some of the layouts I like but to incorporate my chosen images, with the BRYLT commissioner, buttons and a sliding header bar.
I have written a strong brief, I am looking for a website, preferably wordpress as i know they are easy to maintain. I am looking for a one page site, with the top / opening page being full screen image with drop down categories. I have made a rough design, see full brief in word doc attached, there is some freedom to play around with the design aspect but it will need to relay all the content provided. I like a minimal feel. I have also attached some images that may be useful, but will need a new logo for BRYLT Allies. I have attached some logo idea's, it is up to you decide whether you want to use them.
I would prefer the homepage as full screen image, and the categories offered as a drop down or over the main image.
I have also attached linked to some competitors websites:
https://www.verdano-group.co.uk/
http://www.qwmr.org.uk/
Industry/Entity Type
Clinic
Number of Pages Required
1 page
Font styles to use
Look and feel
Each slider illustrates characteristics of the customer's brand and the style your logo design should communicate.

```html
<!DOCTYPE html>
<html lang="en">
<head>
<meta charset="utf-8">
<title>Contact Us – BRYLT Allies</title>
<link rel="stylesheet" href="https://fonts.googleapis.com/css2?family=Open+Sans:wght@400;600&family=Poppins:wght@400;500&family=Arimo:wght@400&display=swap">
<style>
  :root {
    --page-bg: #efefef;
    --white: #ffffff;
    --panel: rgba(255,255,255,0.72);
    --brand-green: #0f967c;
    --brand-purple: #6a1b86;
    --ink: #111111;
    --text: #1e1e1e;
    --icon: #4a4a4a;
    --divider: #e2e2e2;
    --map-tone: #e4e4e4;
    --photo-a: #d8d4cf;
    --photo-b: #8e8a8c;
  }
  * { box-sizing: border-box; margin: 0; padding: 0; }
  html, body { width: 1200px; height: 600px; overflow: hidden; }
  body {
    position: relative;
    background: var(--page-bg);
    font-family: "Open Sans", Arial, sans-serif;
    color: var(--text);
  }
  .brand {
    position: absolute; left: 0; top: 0;
    width: 155px; height: 85px;
    background: var(--white);
    display: flex; align-items: center;
    padding-left: 14px;
  }
  .brand-name {
    display: flex; align-items: center; gap: 8px;
    font-family: "Poppins", sans-serif; font-weight: 500;
    font-size: 26px; line-height: 1; color: var(--brand-purple);
    letter-spacing: 1px;
  }
  .brand-dot { width: 14px; height: 14px; border-radius: 50%; background: var(--brand-green); }
  .side-nav {
    position: absolute; left: 0; top: 85px;
    width: 65px; height: 515px;
    background: var(--white);
  }
  .nav-item {
    position: absolute; left: 0; width: 65px;
    display: flex; align-items: center; justify-content: center;
    border-bottom: 1px solid var(--divider);
  }
  .nav-item svg { width: 28px; height: 28px; stroke: var(--ink); fill: none; stroke-width: 1.4; }
  .nav-item.is-active {
    width: 155px; justify-content: flex-start; gap: 26px;
    padding-left: 20px;
    background: var(--brand-green);
    border-right: 3px solid var(--ink);
    border-bottom: none;
    color: var(--white);
    font-family: "Poppins", sans-serif; font-size: 15px; letter-spacing: .3px;
  }
  .nav-item.is-active svg { stroke: var(--white); width: 24px; height: 24px; }
  .page-title {
    position: absolute; left: 245px; top: 61px;
    font-family: "Arimo", Arial, sans-serif; font-weight: 400;
    font-size: 36px; line-height: 1.15; color: var(--ink);
  }
  .contact-panel {
    position: absolute; left: 235px; top: 118px;
    width: 500px; height: 280px;
    background: var(--panel);
    padding: 25px 0 0 12px;
  }
  .contact-item { margin-bottom: 10px; }
  .contact-label {
    display: flex; align-items: center; gap: 10px;
    font-weight: 600; font-size: 15px; line-height: 20px; height: 20px;
  }
  .contact-label svg { width: 16px; height: 16px; stroke: var(--icon); fill: none; stroke-width: 1.3; }
  .contact-value { padding-left: 26px; margin-top: 10px; font-size: 14px; line-height: 20px; }
  .map-area {
    position: absolute; left: 235px; top: 398px;
    width: 500px; height: 146px;
    background: linear-gradient(135deg, #eaeaea, var(--map-tone) 60%, #dcdcdc);
  }
  .site-footer {
    position: absolute; left: 0; top: 568px; width: 1200px;
    text-align: center;
    font-family: "Poppins", sans-serif; font-size: 11.5px; color: var(--ink);
  }
  .hero-photo { position: absolute; left: 0; top: 0; width: 1200px; height: 600px; pointer-events: none; }
</style>
</head>
<body>

<svg class="hero-photo" viewBox="0 0 1200 600">
  <defs>
    <linearGradient id="photoTone" x1="0" y1="0" x2="0" y2="1">
      <stop offset="0" stop-color="#d8d4cf"/>
      <stop offset="1" stop-color="#8e8a8c"/>
    </linearGradient>
  </defs>
  <path role="img" aria-label="Photo of three smiling young people sitting together on a sofa against a white brick wall"
        d="M1200 68 L860 136 Q838 142 843 166 L936 440 Q958 498 1040 520 L1200 566 Z" fill="url(#photoTone)"/>
  <path d="M1200 58 L852 126 Q826 134 832 166 L928 452" fill="none" stroke="#0f967c" stroke-width="7" stroke-linecap="round"/>
</svg>

<header class="brand">
  <div class="brand-name"><span class="brand-dot"></span>BRYLT</div>
</header>

<nav class="side-nav" aria-label="Main">
  <div class="nav-item" style="top:0;height:87px">
    <svg viewBox="0 0 28 28"><path d="M4 8h20M4 14h20M4 20h20" stroke-width="1.8"/></svg>
  </div>
  <div class="nav-item" style="top:87px;height:76px">
    <svg viewBox="0 0 28 28"><rect x="5" y="5" width="17" height="19"/><path d="M5 9h17M9 3v4M13 3v4M17 3v4M9 19l10-9 2 2-10 9-3 1z"/></svg>
  </div>
  <div class="nav-item" style="top:163px;height:74px">
    <svg viewBox="0 0 28 28"><circle cx="14" cy="10" r="4"/><circle cx="7" cy="13" r="3"/><circle cx="21" cy="13" r="3"/><path d="M7 24v-4a7 7 0 0 1 14 0v4M2 24v-3a5 5 0 0 1 6-5M26 24v-3a5 5 0 0 0-6-5"/></svg>
  </div>
  <div class="nav-item" style="top:237px;height:76px">
    <svg viewBox="0 0 28 28"><path d="M4 20 20 4l4 4L8 24H4zM6 6l16 16-2 2L4 8z"/></svg>
  </div>
  <div class="nav-item is-active" style="top:321px;height:75px">
    <svg viewBox="0 0 24 24"><path d="M5 3l4 1 1 5-2 2a12 12 0 0 0 5 5l2-2 5 1 1 4-3 2C10 21 3 14 3 6z"/></svg>
    CONTACT
  </div>
  <div class="nav-item" style="top:401px;height:80px;border-top:1px solid var(--divider)">
    <svg viewBox="0 0 28 28"><rect x="4" y="4" width="20" height="20"/><path d="M4 10h20M4 16h20M8 7h12M8 13h8M8 19h12"/></svg>
  </div>
</nav>

<h1 class="page-title">Contact Us</h1>

<section class="contact-panel">
  <div class="contact-item">
    <div class="contact-label"><svg viewBox="0 0 16 16"><path d="M3 1.5l3 .8.7 3.4-1.4 1.2a8 8 0 0 0 3.8 3.8l1.2-1.4 3.4.7.8 3-2.2 1.5C6 14 2 10 1.5 3.7z"/></svg>Phone Number</div>
    <div class="contact-value">0203 555 0187</div>
  </div>
  <div class="contact-item">
    <div class="contact-label"><svg viewBox="0 0 16 16"><path d="M8 15s5-5 5-9a5 5 0 0 0-10 0c0 4 5 9 5 9z"/><circle cx="8" cy="6" r="2"/></svg>Address</div>
    <div class="contact-value">Larkfield Suite 2B, 41-47 Mill Lane, London, E19 4XT</div>
  </div>
  <div class="contact-item">
    <div class="contact-label"><svg viewBox="0 0 16 16"><circle cx="8" cy="9" r="5.5"/><path d="M8 6v3l2 1.5M2 3l2.5-1.5M14 3l-2.5-1.5"/></svg>Opening Times</div>
    <div class="contact-value">9am – 5pm Mon-Fri</div>
  </div>
  <div class="contact-item">
    <div class="contact-label"><svg viewBox="0 0 16 16"><rect x="1.5" y="3.5" width="13" height="9"/><path d="M1.5 3.5 8 9l6.5-5.5"/></svg>Email</div>
    <div class="contact-value">enquiry@bryltallies.co.uk</div>
  </div>
</section>

<div class="map-area" role="img" aria-label="Street map showing the clinic location"></div>

<footer class="site-footer">© 2018 All Rights Reserved.brylt.com</footer>

</body>
</html>
```